Dental office stationary (letterhead, envelopes), business cards, presentation folders

Nothing too dental outside of the logo. I will need all stationary, presentation folders, business cards. Would prefer to stay in the colors of the logo

Gordon Pellham, DDS
Brightwell Dental Implant Center
772-555-0187
info@brightwelldental-example.com
3871 NW Corbin Rd Unit B
Stuart, FL 34994

Also need appointment date and time
And cancellation policy
I want it to say “kindly ask for
A 48hr cancellation policy to avoid incurring a cancellation fee”

Industry/Entity Type

Dental

Colors
0054AA
0677BA
7BADD7
CADEEF
E8F1F8

Requirements
Must have
• Name of your office, name of doctor, address, phone number
Should not have
• Too much tooth/dental. Only the tooth in logo

```html
<!DOCTYPE html>
<html lang="en">
<head>
<meta charset="utf-8">
<title>Brightwell Dental Implant Center — Letterhead</title>
<link href="https://fonts.googleapis.com/css2?family=Figtree:wght@400;500;600&display=swap" rel="stylesheet">
<style>
  :root {
    --backdrop: #e6e8ea;
    --paper: #ffffff;
    --ink: #4a4a4a;
    --ink-soft: #666666;
    --salutation: #3a7fc6;
    --brand-cyan: #1fa3dc;
    --brand-teal: #1bbc9f;
    --brand-blue: #0078d2;
  }
  * { box-sizing: border-box; margin: 0; padding: 0; }
  html, body {
    width: 1200px; height: 1200px; overflow: hidden;
    background: var(--backdrop);
    font-family: "Figtree", sans-serif;
  }
  .letterhead {
    position: absolute; left: 190px; top: 41px;
    width: 820px; height: 1117px;
    background: var(--paper);
    overflow: hidden;
    box-shadow: 0 4px 18px rgba(0,0,0,.12);
  }
  .brand-name {
    position: absolute; top: 88px; left: 0; width: 100%;
    text-align: center;
    font-size: 34px; font-weight: 600; letter-spacing: .5px;
    color: var(--brand-teal);
  }
  .salutation {
    position: absolute; left: 58px; top: 250px;
    font-size: 24px; font-weight: 600; color: var(--salutation);
  }
  .letter-body {
    position: absolute; left: 58px; top: 298px; width: 704px;
    font-size: 18.3px; line-height: 25.2px; color: var(--ink);
    text-align: justify;
  }
  .letter-body p + p { margin-top: 25px; }
  .sign-off { position: absolute; left: 67px; top: 768px; }
  .signer-name { font-size: 11.5px; color: var(--ink-soft); }
  .signer-title { font-size: 9px; color: var(--ink-soft); margin-top: 3px; }
  .signature {
    position: absolute; left: 60px; top: 800px;
    width: 180px; height: 88px;
    background: linear-gradient(135deg, #f4f4f4, #e9e9e9);
    border-radius: 4px;
  }
  .contact {
    position: absolute; left: 0; top: 962px; width: 100%;
    text-align: center; color: #333;
  }
  .contact-office { font-size: 21px; color: var(--brand-cyan); line-height: 26px; }
  .contact-row {
    display: flex; justify-content: center; align-items: center; gap: 24px;
    font-size: 19px; line-height: 30px;
  }
  .contact-item { display: inline-flex; align-items: center; gap: 6px; }
  .contact-item svg { fill: var(--brand-cyan); }
  .band-teal { position: absolute; left: 0; top: 1065px; width: 100%; height: 10px; background: var(--brand-teal); }
  .band-blue { position: absolute; left: 0; top: 1081px; width: 100%; height: 36px; background: var(--brand-blue); }
</style>
</head>
<body>
  <main class="letterhead">
    <div class="brand-name">Brightwell Dental Implant Center</div>

    <h1 class="salutation">Dear Mr. John,</h1>

    <div class="letter-body">
      <p>Lorem ipsum dolor sit amet, consectetuer adipiscing elit, sed diam nonummy nibh euismod tincidunt ut laoreet dolore magna aliquam erat volutpat. Ut wisi enim ad minim veniam, quis nostrud exerci tation ullamcorper suscipit lobortis nisl ut aliquip ex ea commodo consequat. Duis autem vel eum iriure dolor in hendrerit in vulputate velit esse molestie consequat, vel illum dolore eu feugiat nulla facilisis at vero eros et accumsan et iusto odio dignissim qui blandit praesent luptatum zzril delenit augue duis dolore te feugait nulla facilisi.</p>
      <p>Lorem ipsum dolor sit amet, cons ectetuer adipiscing elit, sed diam nonummy nibh euismod tincidunt ut laoreet dolore magna aliquam erat volutpat. Ut wisi Lorem ipsum dolor sit amet, consectetuer adipiscing elit, sed diam nonummy nibh euismod tincidunt ut laoreet dolore magna aliquam erat volutpat. Ut wisi enim ad minim veniam, quis nostrud exerci tation ullamcorper suscipit lobortis nisl ut aliquip ex ea commodo consequat. Duis autem vel eum iriure dolor in hendrerit in vulputate velit esse molestie consequat, Lorem ipsum dolor sit amet, cons ectetuer adipiscing elit, sed diam nonummy nibh euismod tincidunt ut laoreet dolore magna aliquam erat volutpat.</p>
    </div>

    <div class="sign-off">
      <div class="signer-name">Dana Mercer</div>
      <div class="signer-title">Office Manager</div>
    </div>
    <div class="signature" role="img" aria-label="Handwritten signature of the office manager"></div>

    <footer class="contact">
      <div class="contact-office">Brightwell Dental Implant Center</div>
      <div class="contact-row">
        <span class="contact-item">
          <svg width="20" height="20" viewBox="0 0 24 24" aria-hidden="true"><path d="M6.6 10.8a15.1 15.1 0 0 0 6.6 6.6l2.2-2.2c.3-.3.7-.4 1-.2 1.1.4 2.3.6 3.6.6.6 0 1 .4 1 1V20c0 .6-.4 1-1 1C10.6 21 3 13.4 3 4c0-.6.4-1 1-1h3.5c.6 0 1 .4 1 1 0 1.3.2 2.5.6 3.6.1.3 0 .7-.2 1l-2.3 2.2z"/></svg>
          772-555-0187
        </span>
        <span class="contact-item">
          <svg width="20" height="14" viewBox="0 0 20 14" aria-hidden="true"><path d="M0 0h20v14H0z M1.5 1.5 10 8l8.5-6.5" fill="var(--brand-cyan)" stroke="#fff" stroke-width="1.4"/></svg>
          info@brightwelldental-example.com
        </span>
      </div>
      <div class="contact-row">
        <span class="contact-item">
          <svg width="14" height="20" viewBox="0 0 14 20" aria-hidden="true"><path d="M7 0a7 7 0 0 0-7 7c0 5 7 13 7 13s7-8 7-13a7 7 0 0 0-7-7zm0 10a3 3 0 1 1 0-6 3 3 0 0 1 0 6z"/></svg>
          3871 NW Corbin Rd Unit B, Stuart, FL 34994
        </span>
      </div>
    </footer>

    <div class="band-teal"></div>
    <div class="band-blue"></div>
  </main>
</body>
</html>
```